Need updated stationery design for chiropractic clinic

We recently moved our office and are looking to refresh our letterhead, business cards, presentation folder and envelopes. I tend to prefer simple, clean designs. We communicate with a lot of attorneys and want to exude professionalism. I have attached our logo and 2 additional versions (all white and white letters instead of grey).

Target Market(s)

Other medical professionals and attorneys. Business cards will go to patients as well.

Industry/Entity Type

Healthcare

```html
<!DOCTYPE html>
<html lang="en">
<head>
<meta charset="utf-8">
<title>Alderpoint Injury Care – Stationery</title>
<link href="https://fonts.googleapis.com/css2?family=Catamaran:wght@500;600;700&family=Arimo:wght@400;700&display=swap" rel="stylesheet">
<style>
  :root {
    --blue: #0099cf;
    --teal: #00cdd2;
    --deep: #0079a8;
    --ink: #3f3f3f;
    --paper: #ffffff;
    --stage: #a4bfdf;
    --brand-font: "Catamaran", sans-serif;
    --body-font: "Arimo", sans-serif;
  }
  * { box-sizing: border-box; margin: 0; padding: 0; }
  html, body { width: 1200px; height: 900px; overflow: hidden; }
  body { background: var(--stage); position: relative; font-family: var(--body-font); color: var(--ink); }

  .sheet { position: absolute; background: var(--paper); overflow: hidden; box-shadow: 0 3px 8px rgba(0,0,0,.25); }
  .decor-area { position: absolute; background: linear-gradient(135deg, var(--teal), var(--blue)); }
  .brand-name { font-family: var(--brand-font); font-weight: 700; color: var(--blue); line-height: 1; white-space: nowrap; }
  .band { position: absolute; background: var(--blue); color: #fff; display: flex; align-items: center; }
  .band-accent { position: absolute; background: var(--teal); }

  /* business card front */
  .card-front { left: 132px; top: 52px; width: 452px; height: 258px; }
  .card-front .decor-area { left: 0; top: 0; width: 258px; height: 226px; }
  .card-front .brand-name { position: absolute; right: 23px; top: 24px; font-size: 31px; }
  .card-front .person { position: absolute; right: 23px; top: 106px; text-align: right; }
  .person-name { font-family: var(--body-font); font-weight: 700; font-size: 17px; color: var(--blue); letter-spacing: .3px; }
  .person-name .surname { color: var(--teal); }
  .person-role { font-size: 13px; margin-top: 2px; }
  .contact-list { list-style: none; position: absolute; right: 23px; top: 162px; text-align: right; font-size: 13px; line-height: 15.5px; }
  .contact-list li { display: flex; justify-content: flex-end; align-items: center; gap: 6px; }
  .contact-list svg { width: 10px; height: 10px; flex: none; }
  .card-front .band { left: 212px; top: 226px; width: 240px; height: 32px; justify-content: flex-end; padding-right: 23px; font-size: 12.5px; }
  .card-front .band-accent { left: 0; top: 226px; width: 206px; height: 32px; }

  /* business card back */
  .card-back { left: 616px; top: 52px; width: 453px; height: 258px; background: var(--blue); display: flex; align-items: center; justify-content: center; }
  .card-back .brand-name { color: var(--deep); font-size: 36px; }

  /* letterhead */
  .letterhead { left: 130px; top: 341px; width: 357px; height: 505px; }
  .letterhead .brand-name { position: absolute; left: 32px; top: 24px; font-size: 17px; }
  .letterhead .contact-list { right: 32px; top: 26px; font-size: 5.6px; line-height: 7px; }
  .letterhead .contact-list svg { width: 5px; height: 5px; }
  .letter-body { position: absolute; left: 32px; top: 155px; width: 292px; }
  .salutation { font-family: var(--brand-font); font-weight: 600; font-size: 9px; margin-bottom: 12px; }
  .letter-body p { font-size: 5.7px; line-height: 7.3px; margin-bottom: 6px; }
  .letter-body .closing { font-family: var(--brand-font); font-weight: 600; font-size: 5px; margin-top: 14px; }
  .signature-area { width: 58px; height: 16px; margin-top: 12px; background: linear-gradient(90deg, #e2e2e2, #f4f4f4); border-radius: 2px; }
  .letterhead .decor-area { left: 0; top: 429px; width: 76px; height: 64px; }
  .letterhead .band { left: 63px; top: 493px; width: 294px; height: 12px; justify-content: center; font-size: 5px; }
  .letterhead .band-accent { left: 0; top: 493px; width: 30px; height: 12px; }

  /* envelope back */
  .envelope-back { left: 518px; top: 346px; width: 552px; height: 240px; }
  .envelope-back svg.flap { position: absolute; left: 0; top: 0; width: 552px; height: 70px; }
  .flap-mark { position: absolute; left: 266px; top: 15px; width: 20px; height: 20px; background: var(--teal); }

  /* envelope front */
  .envelope-front { left: 518px; top: 608px; width: 552px; height: 240px; }
  .envelope-front .brand-name { position: absolute; left: 20px; top: 28px; font-size: 22px; }
  .envelope-front .decor-area { left: 0; top: 138px; width: 102px; height: 85px; }
  .envelope-front .band { left: 85px; top: 223px; width: 467px; height: 17px; justify-content: center; font-size: 7.5px; }
  .envelope-front .band-accent { left: 0; top: 223px; width: 40px; height: 17px; }
</style>
</head>
<body>

<section class="sheet card-front" aria-label="Business card, front">
  <div class="decor-area" role="img" aria-label="Large brand symbol decoration in teal and blue"></div>
  <div class="brand-name">Alderpoint</div>
  <div class="person">
    <div class="person-name">MARCUS <span class="surname">HALE</span></div>
    <div class="person-role">Manager</div>
  </div>
  <ul class="contact-list">
    <li>555-014-2290 <svg viewBox="0 0 10 10"><path d="M2 1l2 2-1 1.3c.6 1.2 1.4 2 2.7 2.7L7 6l2 2-1.3 1.3C4.5 9 1 5.5.7 2.3Z" fill="var(--teal)"/></svg></li>
    <li>hello@alderpointcare.com <svg viewBox="0 0 10 10"><rect x=".8" y="2" width="8.4" height="6" fill="none" stroke="var(--teal)" stroke-width="1"/><path d="M.8 2 5 5.5 9.2 2" fill="none" stroke="var(--teal)" stroke-width="1"/></svg></li>
    <li>www.alderpointcare.com <svg viewBox="0 0 10 10"><circle cx="5" cy="5" r="4.2" fill="none" stroke="var(--teal)" stroke-width="1"/><path d="M.8 5h8.4M5 .8c-2 2.5-2 5.9 0 8.4M5 .8c2 2.5 2 5.9 0 8.4" fill="none" stroke="var(--teal)" stroke-width=".8"/></svg></li>
  </ul>
  <div class="band-accent"></div>
  <div class="band">Your address, city, state, ZIP 0000</div>
</section>

<section class="sheet card-back" aria-label="Business card, back">
  <div class="brand-name">Alderpoint</div>
</section>

<section class="sheet letterhead" aria-label="Letterhead">
  <div class="brand-name">Alderpoint</div>
  <ul class="contact-list">
    <li>555-014-2290 <svg viewBox="0 0 10 10"><path d="M2 1l2 2-1 1.3c.6 1.2 1.4 2 2.7 2.7L7 6l2 2-1.3 1.3C4.5 9 1 5.5.7 2.3Z" fill="var(--teal)"/></svg></li>
    <li>hello@alderpointcare.com <svg viewBox="0 0 10 10"><rect x=".8" y="2" width="8.4" height="6" fill="none" stroke="var(--teal)" stroke-width="1"/><path d="M.8 2 5 5.5 9.2 2" fill="none" stroke="var(--teal)" stroke-width="1"/></svg></li>
    <li>www.alderpointcare.com <svg viewBox="0 0 10 10"><circle cx="5" cy="5" r="4.2" fill="none" stroke="var(--teal)" stroke-width="1"/><path d="M.8 5h8.4M5 .8c-2 2.5-2 5.9 0 8.4M5 .8c2 2.5 2 5.9 0 8.4" fill="none" stroke="var(--teal)" stroke-width=".8"/></svg></li>
  </ul>
  <div class="letter-body">
    <div class="salutation">Dear Mr. Hale,</div>
    <p>Lorem ipsum dolor sit amet, consectetuer adipiscing elit, sed diam nonummy nibh euismod tincidunt ut laoreet dolore magna aliquam erat volutpat. Ut wisi enim ad minim veniam, quis nostrud exerci tationmcorper suscipit lobortis nisl ut aliquip ex ea commodo consequat. Duis autem vel eum iriure dolor in hendrerit in vulputate velit esse molestie consequat, vel illum dolore eu feugiat</p>
    <p>Rorem ipsum dolor sit amet, consectetuer adipiscing elit, sed diam nonummy nibh euismod tincidunt ut laoreet dolore magna aliquam erat volutpat. Ut wisi enim ad minim veniam, quis nostrud exerci tationmcorper suscipit lobortis nisl ut aliquip ex ea commodo consequat. Duis autem vel eum iriure dolor in hendrerit in vulputate velit esse molest</p>
    <p>Dorem ipsum dolor sit amet, consectetuer adipiscing elit, sed diam nonummy nibh euismod tincidunt ut laoreet dolore magna aliquam erat volutpat. Ut wisi enim ad minim veniam, quis nostrud exerci tationmcorper suscipit lobortis nisl ut aliquip ex ea commodo consequat. Duis autem vel eum iriure dolor in hendrerit in suscipit lobortis nisl ut aliquip ex ea commodo consequat. Duis autem vel eum iriure dolor in hendrerit in vulputate velit esse molestie consequat, vel illum</p>
    <p>Sorem ipsum dolor sit amet, consectetuer adipiscing elit, sed diam nonummy nibh euismod tincidunt ut laoreet dolore magna aliquam erat volutpat. Ut wisi enim ad minim veniam, quis nostrud exerci tationmcorper suscipit lobortis nisl ut aliquip ex ea commodo consequat. Duis autem vel eum iriure dolor in</p>
    <div class="closing">Sincerely,</div>
    <div class="signature-area" role="img" aria-label="Handwritten signature"></div>
  </div>
  <div class="decor-area" role="img" aria-label="Brand symbol decoration in teal and blue"></div>
  <div class="band-accent"></div>
  <div class="band">Your address, city, state, ZIP 0000</div>
</section>

<section class="sheet envelope-back" aria-label="Envelope, back">
  <svg class="flap" viewBox="0 0 552 70" aria-hidden="true">
    <path d="M1 1 L12 50 Q16 66 34 66 L518 66 Q536 66 540 50 L551 1" fill="#fff" stroke="#d8d8d8" stroke-width="1.2"/>
  </svg>
  <div class="flap-mark"></div>
</section>

<section class="sheet envelope-front" aria-label="Envelope, front">
  <div class="brand-name">Alderpoint</div>
  <div class="decor-area" role="img" aria-label="Brand symbol decoration in teal and blue"></div>
  <div class="band-accent"></div>
  <div class="band">Your address, city, state, ZIP 0000</div>
</section>

</body>
</html>
```